Brisk Tutorium Website

We are looking for a new design of our website. The current website is www.brisktutorium.example. The company is the #1 pre-college math and science program in Bayfield County, CA. We would like to see designs that integrate our logo with a modern color scheme. We are also open for suggestions that could improve our logo. We would like a simple, minimal, clean, classy, and vibrant front-page user interface design that give the premium, modern, innovative, creative, and premier brand feel. We like the "New Retro Colors for the Web" as described here: http://www.pixel-layoutnook.example/en/layout-notes-2013/.

Target Market(s)

The target market is parents with K-12 students from a diverse population. Parents are well educated with family income > $150,000. Most of the decision makers are mothers from immigrate families: 30% Chinese, 30% Korean, 15% Indian, 24% White.

Industry/Entity Type

College

Requirements
Must have
• Must read our statement of differentiation at:
• http://brisktutorium.example/about-us
• Your design must be reflective of your understanding of the statements.
Nice to have
• The design should also be mobil friendly.
Should not have
• While most of our current classes are math, our company is expanding to include STEM (Science, Technology, Engineering, and Math) for gifted students. Therefore, the site should not be JUST a math education site.

```html
<!DOCTYPE html>
<html lang="en">
<head>
<meta charset="utf-8">
<title>Brisk Tutorium for Gifted Youth</title>
<link href="https://fonts.googleapis.com/css2?family=Metrophobic&display=swap" rel="stylesheet">
<style>
:root{
  --topbar:#3b3b3b;
  --ink:#2b2b2b;
  --green:#5a9e2c;
  --green-dark:#4f8f2c;
  --brand:#3f4aa0;
  --nav-active:#f29a2e;
  --link:#f29a2e;
  --rule:#bdbdbd;
  --hero-a:#98c86e;
  --hero-b:#6fa848;
  --tile1-a:#f47b52;--tile1-b:#d6502b;
  --tile2-a:#6ad8db;--tile2-b:#3cb2b5;
  --tile3-a:#f7bc55;--tile3-b:#e79a2b;
  --tile4-a:#e48a9c;--tile4-b:#c75e6e;
  --cal-grey:#d9d9d9;
  --today:#c8e6b4;
}
*{box-sizing:border-box;margin:0;padding:0}
html,body{width:1200px;height:1109px;overflow:hidden}
body{position:relative;background:#fff;font-family:"Metrophobic",sans-serif;color:var(--ink)}
.abs{position:absolute}
.topbar{left:0;top:0;width:1200px;height:32px;background:var(--topbar)}
.util{right:270px;top:9px;font-size:13px;color:#eee;display:flex;gap:14px}
.util span.sep{color:#aaa}
.search{left:954px;top:6px;width:153px;height:22px;background:#fff;font-size:12px;color:#777;padding:4px 6px}
.search svg{position:absolute;right:8px;top:3px}
.header{left:0;top:32px;width:1200px;height:83px;background:#fff;border-bottom:1px solid #ddd}
.brand{left:90px;top:50px;display:flex;align-items:center;gap:10px;color:var(--brand)}
.brand .mark{width:50px;height:50px;border-radius:50%;background:var(--brand)}
.brand .name{font-size:24px;line-height:24px}
.brand .tag{font-size:14px;letter-spacing:1px;line-height:16px;padding-left:14px}
.nav{left:387px;top:32px;height:83px;display:flex}
.nav a{font-size:12.5px;color:#444;text-decoration:none;text-align:center;line-height:83px;border-left:1px solid #e6e6e6;white-space:nowrap}
.nav a:first-child{border-left:none;color:var(--nav-active)}
.hero{left:0;top:115px;width:1200px;height:313px;background:radial-gradient(ellipse at 45% 40%,var(--hero-a),var(--hero-b))}
.hero h1{position:absolute;right:762px;top:100px;font-weight:400;font-size:26px;color:#fff;text-shadow:1px 1px 2px rgba(0,0,0,.35);white-space:nowrap}
.hero p{position:absolute;right:762px;top:138px;font-size:17px;line-height:23px;color:#fff;text-align:right;text-shadow:1px 1px 2px rgba(0,0,0,.35)}
.dots{position:absolute;left:408px;top:197px;display:flex;gap:4px}
.dots i{width:7px;height:7px;border-radius:50%;background:#fff}
.dots i:first-child{background:#b6e05a}
.hero .photo{position:absolute;left:530px;top:15px;width:530px;height:298px;background:linear-gradient(180deg,#a9c98f 0%,#5b6070 55%,#2f3346 100%);border-radius:120px 120px 0 0}
.tiles{left:90px;top:428px;width:1016px;height:199px;display:flex}
.tile{width:254px;height:199px;color:#fff;text-align:center;padding:28px 18px 0}
.tile svg{display:block;margin:0 auto;height:42px}
.tile h2{font-weight:400;font-size:19px;line-height:22px;color:#222;margin:14px 0 12px}
.tile p{font-size:12.5px;line-height:15.5px}
.t1{background:linear-gradient(var(--tile1-a),var(--tile1-b))}
.t2{background:linear-gradient(var(--tile2-a),var(--tile2-b))}
.t3{background:linear-gradient(var(--tile3-a),var(--tile3-b))}
.t4{background:linear-gradient(var(--tile4-a),var(--tile4-b))}
.t2 h2{margin-bottom:9px}.t2 p{line-height:13.5px;font-size:12px}
.main{left:90px;top:658px;width:732px}
.main h3{font-weight:400;font-size:19px;color:var(--green);margin-bottom:8px}
.main p{font-size:12.5px;line-height:16px;color:#222}
.main a{color:var(--link)}
.main hr{border:none;border-top:1px dashed var(--rule);margin:30px 0 22px}
.intro{display:flex;gap:10px}
.intro .badge{flex:none;width:114px;height:95px;border:1px solid #ddd;display:flex;align-items:center;justify-content:center;text-align:center;color:var(--brand);font-size:15px;line-height:18px}
.side{left:852px;width:256px}
.events{top:653px;height:148px;border:1px solid #ddd}
.events h4{font-weight:400;background:var(--green-dark);color:#fff;font-size:19px;height:37px;line-height:36px;padding-left:12px}
.event{display:flex;gap:10px;padding:11px 12px 0}
.event .thumb{width:93px;height:62px;flex:none;background:linear-gradient(135deg,#e3a24b,#3d68a8 60%,#c9403c)}
.event b{font-weight:400;font-size:13px;display:block}
.event p{font-size:12.5px;line-height:16px}
.event .date{color:var(--link)}
.pager{position:absolute;left:0;right:0;top:122px;border-top:1px dashed var(--rule);display:flex;justify-content:space-between;padding:5px 12px;font-size:11px}
.cal{top:825px;height:170px;border:1px solid #ddd}
.cal .head{height:32px;background:var(--green-dark);color:#fff;font-size:13px;text-align:center;line-height:32px;position:relative}
.cal .head svg{position:absolute;top:9px}
.cal table{width:100%;border-collapse:collapse;font-size:12px;text-align:center}
.cal td,.cal th{font-weight:400;height:22.6px}
.cal tr.g{background:var(--cal-grey)}
.cal td.today{background:var(--today)}
.newslabel{top:1006px;font-size:13px;color:var(--green)}
.news{top:1028px;height:90px;border:1px solid #ddd;padding:13px 9px;font-size:12.5px;line-height:15px}
.news .date{display:block;text-align:right;color:var(--link);margin-top:3px;padding-right:22px}
</style>
</head>
<body>
<div class="abs topbar"></div>
<div class="abs util"><span>Sitemap</span><span class="sep">|</span><span>Accessibility</span><span class="sep">|</span><span>Contact</span></div>
<div class="abs search">Search...
<svg width="16" height="16" viewBox="0 0 16 16"><circle cx="6.5" cy="6.5" r="5" fill="none" stroke="#888" stroke-width="1.5"/><path d="M10 10l5 5" stroke="#888" stroke-width="2"/></svg></div>

<header class="abs header"></header>
<div class="abs brand"><span class="mark"></span><div><div class="name">Brisk Tutorium</div><div class="tag">for Gifted Youth</div></div></div>
<nav class="abs nav">
<a style="width:60px">Home</a><a style="width:76px">About Us</a><a style="width:52px">Math</a><a style="width:62px">Physics</a><a style="width:83px">Chemistry</a><a style="width:67px">Biology</a><a style="width:92px">Science Fair</a><a style="width:72px">Fall 2013</a><a style="width:104px">Summer 2013</a><a style="width:60px">Results</a>
</nav>

<section class="abs hero">
<h1>Welcome to our site</h1>
<p>Math Olympiad and Problem<br>Solving Training Programs</p>
<div class="dots"><i></i><i></i><i></i></div>
<div class="photo" role="img" aria-label="Photo of four smiling students in school blazers raising fists"></div>
</section>

<section class="abs tiles">
<div class="tile t1">
<svg width="44" height="40" viewBox="0 0 44 40"><rect x="6" y="2" width="32" height="26" rx="3" fill="#fff"/><rect x="11" y="7" width="22" height="16" fill="#e0643b"/><rect x="1" y="30" width="42" height="7" rx="2" fill="#fff"/></svg>
<h2>eLearning</h2><p>Click on eLearning to access our Online Learning Management System for current students and families.</p></div>
<div class="tile t2">
<svg width="44" height="44" viewBox="0 0 44 44"><circle cx="22" cy="22" r="20" fill="#fff"/><path d="M22 10v12l8 6" stroke="#4cc0c3" stroke-width="3" fill="none"/><circle cx="22" cy="6" r="1.5" fill="#4cc0c3"/><circle cx="22" cy="38" r="1.5" fill="#4cc0c3"/><circle cx="6" cy="22" r="1.5" fill="#4cc0c3"/><circle cx="38" cy="22" r="1.5" fill="#4cc0c3"/></svg>
<h2>Scheduler</h2><p>Click on Scheduler to make an appointment online for qualifying exams, gathering information, college counseling, or science research meetings.</p></div>
<div class="tile t3">
<svg width="44" height="40" viewBox="0 0 44 40"><rect x="8" y="2" width="34" height="34" rx="3" fill="#fff"/><rect x="2" y="10" width="8" height="26" rx="3" fill="#fff"/><rect x="13" y="8" width="12" height="10" fill="#eda63a"/><path d="M28 10h10M28 16h10M13 23h25M13 29h25" stroke="#eda63a" stroke-width="3"/></svg>
<h2>Newsletter</h2><p>Click on Newsletter to subscribe to our monthly newsletter - The Brisk Learner.</p></div>
<div class="tile t4">
<svg width="46" height="42" viewBox="0 0 46 42"><rect x="3" y="6" width="32" height="32" rx="2" fill="none" stroke="#fff" stroke-width="5"/><path d="M11 20l8 8 22-24" stroke="#fff" stroke-width="6" fill="none"/></svg>
<h2>Registration</h2><p>Click on Registration to sign up for our classes.</p></div>
</section>

<main class="abs main">
<h3>Math Olympiad and Problem Solving Training Programs</h3>
<p>Welcome to Brisk Tutorium for Gifted Youth. We provide after-school enrichment programs in math, physics, chemistry, biology, and computer science, mentor middle and high school science research projects, and offer college counseling to aspiring students in pursuing their college dreams. Please explore this website to learn more about our programs and our approach to gifted education.</p>
<hr>
<h3>Why Brisk Tutorium for Gifted Youth?</h3>
<div class="intro"><div class="badge">Brisk Tutorium<br>Online</div>
<p>In 2005, Brisk Tutorium for Gifted Youth was the first academy to offer advanced math problem solving to gifted students in Bayfield County. With its roots in the Westbrook math community and locations proximate to Coastal State University and Harborview College, Brisk Tutorium for Gifted Youth combines State Standardized Mathematics Curriculum with math competitions and problem solving to help gifted students to discover their passion, develop their skills, and fulfill their college dreams. To learn more about our philosophy, history, statement of differentiation, and approach to gifted education, <a>click here</a>.</p></div>
<hr style="margin-top:22px">
<h3>Brisk eLearning - A Blended Learning Platform</h3>
<p>We are pleased to announce the launch of Brisk Tutorium eLearning Center - an online community for students and parents to learn and share knowledge. With the eLearning Center, students have access to additional learning resources, can review classroom materials, download homework solutions, view grade reports, and share knowledge and communicate with other classmates in a safe and protected environment. Parents will be able to monitor their children's learning progress and participate in forum discussions related to gifted education and math talent development. <a>Click here</a> to learn more.</p>
</main>

<aside>
<div class="abs side events">
<h4>Upcoming Events</h4>
<div class="event"><div class="thumb" role="img" aria-label="Photo of colourful books and supplies"></div>
<div><b>MCT 8</b><p>Write something about this program.</p><p class="date">TBD, 19-11-2013</p></div></div>
<div class="pager"><span>&lt; Prev Events</span><span>Upcoming Events &gt;</span></div>
</div>
<div class="abs side cal">
<div class="head"><svg style="left:10px" width="10" height="14" viewBox="0 0 10 14"><path d="M8 1L2 7l6 6" stroke="#fff" stroke-width="2" fill="none"/></svg>AUGUST 2013<svg style="right:10px" width="10" height="14" viewBox="0 0 10 14"><path d="M2 1l6 6-6 6" stroke="#fff" stroke-width="2" fill="none"/></svg></div>
<table>
<tr class="g"><th>Su</th><th>Mo</th><th>Tu</th><th>We</th><th>Th</th><th>Fr</th><th>Sa</th></tr>
<tr><td></td><td></td><td></td><td></td><td>1</td><td>2</td><td>3</td></tr>
<tr class="g"><td>4</td><td>5</td><td>6</td><td>7</td><td>8</td><td>9</td><td>10</td></tr>
<tr><td>11</td><td>12</td><td class="today">13</td><td>14</td><td>15</td><td>16</td><td>17</td></tr>
<tr class="g"><td>18</td><td>19</td><td>20</td><td>21</td><td>22</td><td>23</td><td>24</td></tr>
<tr><td>25</td><td>26</td><td>27</td><td>28</td><td>29</td><td>30</td><td>31</td></tr>
</table>
</div>
<div class="abs side newslabel">Latest News :</div>
<div class="abs side news">2013 College matriculation list has been published. See our notice board for further details.<span class="date">13-08-2013</span></div>
</aside>
</body>
</html>
```